Upmark Velo

We are a new start up company selling (online) innovative cycling products.
Being a new player in the market a modern eye catching logo would be good.
Initially selling safety tail lights with blinkers & modern designed cycling gloves and eventually extending our range into cycling clothing. Many of our products will have a safety theme.

Please see logo attached.
Updates

Project Deadline Extended
Reason: I have extended deadline because i have just received the Logo to be used.

Target Market(s)

We will be target marketing to the young 20-30year old trendy commuter cyclists to the 40 - 60 year old weekend road riders with there immaculate color coordinated road bikes & clothing.

Industry/Entity Type

Safety

Requirements
Must have
• Name: Liam Beck
Line for Mobile No. 0468 923 051
Line for email Address: liam@upmarkvelo.com.au
3 Lines for Postal Address: PO Box 3826
Harlow Vale Crossing
NSW 2157
Website: www.upmarkvelo.com.au

```html
<!DOCTYPE html>
<html lang="en">
<head>
<meta charset="utf-8">
<title>Upmark Velo – Business Card</title>
<link rel="stylesheet" href="https://fonts.googleapis.com/css2?family=Arimo:wght@700&display=swap">
<style>
  :root {
    --page-bg: #e9e7e3;
    --card-white: #ffffff;
    --card-black: #1b1b1b;
    --accent-orange: #f08a12;
    --text-dark: #1b1b1b;
    --text-light: #ffffff;
  }
  * { margin: 0; padding: 0; box-sizing: border-box; }
  html, body {
    width: 1200px;
    height: 918px;
    overflow: hidden;
    background: var(--page-bg);
    font-family: "Arimo", Arial, sans-serif;
    font-weight: 700;
  }
  .business-card {
    position: absolute;
    left: 100px;
    top: 173px;
    width: 1000px;
    height: 571px;
    background: var(--card-white);
    overflow: hidden;
    box-shadow: 0 6px 24px rgba(0,0,0,0.18);
  }
  .card-shapes {
    position: absolute;
    inset: 0;
    width: 100%;
    height: 100%;
  }
  .card-shapes .dark-field { fill: var(--card-black); }
  .card-shapes .accent-curve { fill: none; stroke: var(--accent-orange); stroke-width: 6; }

  .brand {
    position: absolute;
    right: 52px;
    top: 150px;
    display: flex;
    align-items: flex-end;
    gap: 14px;
  }
  .brand-name {
    font-size: 46px;
    color: var(--text-dark);
    letter-spacing: -0.5px;
    line-height: 1;
  }
  .brand-dot {
    width: 30px;
    height: 30px;
    border-radius: 50%;
    background: var(--accent-orange);
    margin-bottom: 30px;
  }
  .person {
    position: absolute;
    right: 52px;
    top: 218px;
    text-align: right;
  }
  .person-name {
    font-size: 38px;
    color: var(--text-dark);
    line-height: 1.05;
  }
  .person-title {
    font-size: 17px;
    color: var(--accent-orange);
    margin-top: 2px;
  }

  .contact-list {
    position: absolute;
    left: 62px;
    top: 262px;
    list-style: none;
    color: var(--text-light);
    font-size: 25px;
    line-height: 1.2;
  }
  .contact-item {
    display: flex;
    align-items: flex-start;
    gap: 22px;
    margin-bottom: 12px;
  }
  .contact-icon {
    flex: 0 0 38px;
    width: 38px;
    height: 38px;
    border-radius: 50%;
    background: var(--text-light);
    display: flex;
    align-items: center;
    justify-content: center;
  }
  .contact-icon svg { width: 22px; height: 22px; }
  .contact-icon svg * { fill: none; stroke: var(--card-black); stroke-width: 2; }
  .contact-icon svg .solid { fill: var(--card-black); stroke: none; }
  .contact-text { padding-top: 5px; }
  .contact-item.repeat { padding-left: 60px; }
</style>
</head>
<body>
  <div class="business-card">
    <svg class="card-shapes" viewBox="0 0 1000 571" preserveAspectRatio="none" aria-hidden="true">
      <path class="dark-field" d="M0 0 L40 0 C250 230 600 345 1000 362 L1000 571 L0 571 Z"/>
      <path class="accent-curve" d="M52 -4 C262 222 610 333 1004 348"/>
    </svg>

    <div class="brand">
      <span class="brand-name">Upmark Velo</span>
      <span class="brand-dot"></span>
    </div>

    <div class="person">
      <div class="person-name">Liam Beck</div>
      <div class="person-title">M.D.</div>
    </div>

    <ul class="contact-list">
      <li class="contact-item">
        <span class="contact-icon">
          <svg viewBox="0 0 24 24"><path d="M12 22s7-7.5 7-12.5A7 7 0 0 0 5 9.5C5 14.5 12 22 12 22z"/><circle cx="12" cy="9.5" r="2.5"/></svg>
        </span>
        <span class="contact-text">PO Box 3826<br>Harlow Vale Crossing<br>NSW 2157</span>
      </li>
      <li class="contact-item">
        <span class="contact-icon">
          <svg viewBox="0 0 24 24"><rect x="7" y="2.5" width="10" height="19" rx="2"/><circle class="solid" cx="12" cy="18" r="1.2"/></svg>
        </span>
        <span class="contact-text">0468 923 051</span>
      </li>
      <li class="contact-item">
        <span class="contact-icon">
          <svg viewBox="0 0 24 24"><rect x="3" y="6" width="18" height="12" rx="1"/><path d="M3 6l9 7 9-7"/></svg>
        </span>
        <span class="contact-text">liam@upmarkvelo.com.au</span>
      </li>
      <li class="contact-item">
        <span class="contact-icon">
          <svg viewBox="0 0 24 24"><circle cx="12" cy="12" r="9"/><ellipse cx="12" cy="12" rx="4" ry="9"/><path d="M3 12h18"/></svg>
        </span>
        <span class="contact-text">www.upmarkvelo.com.au</span>
      </li>
      <li class="contact-item repeat">
        <span class="contact-text">www.upmarkvelo.com.au</span>
      </li>
    </ul>
  </div>
</body>
</html>
```